Pell Consulting -New consulting business in architecture, urban planning, and real estate development

We need a stationery design, including logo, business cards, etc, work for a new consulting business that works in the world of architectural, urban planning and real estate development.

The name of the company is "Pell Consulting". Pell is my last name but it of course also has the meaning 'cool' and 'hip'.

Target Market(s)

The business will provide boutique consulting services to high end clients that may include property developers, cities, etc.

Industry/Entity Type

Consultant

Contact Information for Business Card

PELL Consulting
First Name Last Name
Title
Phone number
Address
Website
Optional: Twitter handle

Logo Text

PELL Consulting

Font styles to use
Sans Serif

Colors

Designer to choose colors to be used in the design.

Requirements
Must have
• Simple design
• Easy to read font
• Modern
• Elegance
• Nice font that can be used for future reports, letters, etc.
• Good colour scheme that allows for the elegance to come through
Should not have
• Complex design ideas
• Complex logos
• Not a corporate feel and look

```html
<!DOCTYPE html>
<html lang="en">
<head>
<meta charset="utf-8">
<title>Pell Consulting – Stationery</title>
<link href="https://fonts.googleapis.com/css2?family=Roboto+Slab:wght@700&family=Roboto:wght@400;500&display=swap" rel="stylesheet">
<style>
  :root {
    --navy: #0f3340;
    --olive: #b3b73b;
    --olive-faint: #eef0d9;
    --grey-faint: #e3e6e6;
    --ink: #333536;
    --muted: #8a8c8d;
    --paper: #f3f3f3;
    --white: #ffffff;
    --backdrop: #e9e9e9;
  }
  * { box-sizing: border-box; margin: 0; padding: 0; }
  html, body { width: 1200px; height: 1099px; overflow: hidden; }
  body {
    position: relative;
    background: radial-gradient(ellipse at 40% 60%, #f6f6f6 0%, var(--backdrop) 70%, #dcdcdc 100%);
    font-family: "Roboto", Arial, sans-serif;
    color: var(--ink);
  }
  .brand { position: absolute; display: flex; align-items: center; }
  .brand-square { background: var(--olive); flex: none; }
  .brand-name { font-family: "Roboto Slab", Georgia, serif; font-weight: 700; color: var(--ink); line-height: 1; }
  .brand-sub { font-family: "Roboto", Arial, sans-serif; color: var(--muted); letter-spacing: .12em; line-height: 1; }

  .brand-main { left: 70px; top: 62px; gap: 18px; }
  .brand-main .brand-square { width: 58px; height: 58px; }
  .brand-main .brand-name { font-size: 36px; }
  .brand-main .brand-sub { font-size: 26px; margin-top: 6px; }

  .sheet { position: absolute; box-shadow: 0 2px 8px rgba(0,0,0,.18); overflow: hidden; }

  /* business cards */
  .card { width: 340px; height: 196px; border-radius: 12px; background: #f1f1f1; }
  .card-front { left: 70px; top: 210px; }
  .card-back { left: 150px; top: 440px; }
  .card .brand { gap: 8px; }
  .card .brand-square { width: 20px; height: 20px; }
  .card .brand-name { font-size: 15px; }
  .card .brand-sub { font-size: 10px; margin-top: 3px; }
  .card-front .brand { right: 20px; top: 22px; }
  .card-person { position: absolute; left: 22px; top: 72px; }
  .card-person .name { font-family: "Roboto Slab", Georgia, serif; font-weight: 700; font-size: 12px; }
  .card-person .role { font-size: 9px; color: var(--muted); }
  .card-details { position: absolute; left: 22px; top: 112px; font-size: 9px; line-height: 1.45; color: #555; }
  .card-bands { position: absolute; left: 0; right: 0; bottom: 0; height: 12px; }
  .card-back .brand { left: 88px; top: 72px; }
  .card-back .brand-square { width: 28px; height: 28px; }
  .card-back .brand-name { font-size: 20px; }
  .card-back .brand-sub { font-size: 12px; }
  .card-web { position: absolute; left: 124px; top: 128px; font-size: 10px; color: var(--olive); }

  /* letterhead */
  .letter { width: 406px; height: 574px; background: var(--paper); }
  .letter-under { left: 695px; top: 82px; }
  .letter-top { left: 667px; top: 115px; }
  .letter .brand { left: 30px; top: 28px; gap: 8px; }
  .letter .brand-square { width: 24px; height: 24px; }
  .letter .brand-name { font-size: 14px; }
  .letter .brand-sub { font-size: 10px; margin-top: 2px; }
  .faint-square { position: absolute; }
  .letter .faint-square { left: 246px; top: 350px; width: 140px; height: 160px; background: var(--olive-faint); }
  .letter-contact { position: absolute; left: 32px; top: 500px; font-size: 8.5px; line-height: 1.5; color: #444; }
  .letter-address { position: absolute; right: 30px; top: 514px; font-size: 8.5px; line-height: 1.3; text-align: right; color: #444; }
  .letter-bands { position: absolute; left: 0; right: 0; bottom: 0; height: 16px; }

  /* envelope */
  .envelope { top: 739px; height: 291px; background: var(--white); }
  .envelope-front { left: 69px; width: 585px; }
  .envelope-back { left: 654px; width: 446px; }
  .envelope-front .brand { left: 42px; top: 36px; gap: 10px; }
  .envelope-front .brand-square { width: 36px; height: 36px; }
  .envelope-front .brand-name { font-size: 18px; }
  .envelope-front .brand-sub { font-size: 12px; margin-top: 3px; }
  .envelope-address { position: absolute; right: 48px; top: 216px; font-size: 10px; line-height: 1.3; text-align: right; color: #444; }
  .envelope-phone { position: absolute; right: 48px; top: 244px; font-size: 11px; color: #444; }
  .envelope-bands { position: absolute; left: 0; right: 0; bottom: 0; height: 24px; }
  .envelope-flap { position: absolute; left: 0; top: 0; width: 446px; height: 110px; }
  .envelope-back .flap-mark { position: absolute; left: 176px; top: 30px; width: 34px; height: 34px; background: #d4d77f; }
  .envelope-back .faint-square { left: 340px; top: 180px; width: 70px; height: 80px; background: var(--olive-faint); }
</style>
</head>
<body>

  <header class="brand brand-main">
    <span class="brand-square"></span>
    <div>
      <div class="brand-name">Pell Consulting</div>
      <div class="brand-sub">Architectural</div>
    </div>
  </header>

  <!-- business card: contact side -->
  <section class="sheet card card-front">
    <div class="brand">
      <span class="brand-square"></span>
      <div>
        <div class="brand-name">Pell Consulting</div>
        <div class="brand-sub">Architectural</div>
      </div>
    </div>
    <div class="card-person">
      <div class="name">Owen Hartley</div>
      <div class="role">Sales Manager</div>
    </div>
    <div class="card-details">
      14/82 Harbour View Road<br>
      Eastwood NSW 2122<br>
      ☏ 1300 727 318<br>
      ✆ 0451 264 907<br>
      @ info@pellconsulting.com
    </div>
    <svg class="card-bands" viewBox="0 0 340 12" preserveAspectRatio="none">
      <polygon points="0,0 245,0 257,12 0,12" fill="var(--olive)"/>
      <polygon points="262,4 340,4 340,12 270,12" fill="var(--navy)"/>
    </svg>
  </section>

  <!-- business card: brand side -->
  <section class="sheet card card-back">
    <div class="brand">
      <span class="brand-square"></span>
      <div>
        <div class="brand-name">Pell Consulting</div>
        <div class="brand-sub">Architectural</div>
      </div>
    </div>
    <div class="card-web">www.pellconsulting.com</div>
  </section>

  <!-- letterhead -->
  <section class="sheet letter letter-under">
    <svg class="letter-bands" viewBox="0 0 406 16" preserveAspectRatio="none">
      <polygon points="310,6 406,6 406,16 318,16" fill="var(--navy)"/>
    </svg>
  </section>
  <section class="sheet letter letter-top">
    <div class="brand">
      <span class="brand-square"></span>
      <div>
        <div class="brand-name">Pell Consulting</div>
        <div class="brand-sub">Architectural</div>
      </div>
    </div>
    <div class="faint-square" aria-hidden="true"></div>
    <div class="letter-contact">
      ☏ 1300 727 318<br>
      ✆ 0451 264 907<br>
      @ info@pellconsulting.com
    </div>
    <div class="letter-address">
      14/82 Harbour View Road<br>
      Eastwood NSW 2122
    </div>
    <svg class="letter-bands" viewBox="0 0 406 16" preserveAspectRatio="none">
      <polygon points="0,0 294,0 310,16 0,16" fill="var(--olive)"/>
      <polygon points="300,6 406,6 406,16 310,16" fill="var(--navy)"/>
    </svg>
  </section>

  <!-- envelope front -->
  <section class="sheet envelope envelope-front">
    <div class="brand">
      <span class="brand-square"></span>
      <div>
        <div class="brand-name">Pell Consulting</div>
        <div class="brand-sub">Architectural</div>
      </div>
    </div>
    <div class="envelope-address">
      14/82 Harbour View Road<br>
      Eastwood NSW 2122
    </div>
    <div class="envelope-phone">1300 727 318 ☏</div>
    <svg class="envelope-bands" viewBox="0 0 585 24" preserveAspectRatio="none">
      <polygon points="0,0 412,0 436,24 0,24" fill="var(--olive)"/>
      <polygon points="430,8 585,8 585,24 446,24" fill="var(--navy)"/>
    </svg>
  </section>

  <!-- envelope back -->
  <section class="sheet envelope envelope-back">
    <svg class="envelope-flap" viewBox="0 0 446 110" preserveAspectRatio="none">
      <path d="M0,0 H446 Q440,38 420,44 L180,100 Q160,106 140,102 L0,74 Z" fill="var(--olive)"/>
    </svg>
    <div class="flap-mark" aria-hidden="true"></div>
    <div class="faint-square" aria-hidden="true"></div>
  </section>

</body>
</html>
```